Business Card for Brevel Coatings

We need a simple, yet out standing business card for our painting company.

Target Market(s)

wealthy; high-end neighborhoods, and businesses

Industry/Entity Type

Painting

Contact Information for Business Card

Name:
Doran Vask

Email:
d.vask@brevel-coatings.com

Website:
Brevel-coatings.com

Phone Number:
(555) 416-9073

Font styles to use
Serif
Sans Serif

Requirements
Must have
• slogan "making change simple"
Should not have
• A title attached to the name on the card

```html
<!DOCTYPE html>
<html lang="en">
<head>
<meta charset="utf-8">
<title>Brevel Coatings – Business Card</title>
<link rel="stylesheet" href="https://fonts.googleapis.com/css2?family=Open+Sans:wght@400;600&display=swap">
<style>
  :root {
    --backdrop: #8e8e8e;
    --card-white: #f3f3f1;
    --green-dark: #2f4606;
    --green-light: #8cb42c;
    --text-grey: #575757;
    --text-light: #e9ece4;
  }
  * { margin: 0; padding: 0; box-sizing: border-box; }
  html, body { width: 1105px; height: 1200px; overflow: hidden; }
  body {
    background: var(--backdrop);
    font-family: "Open Sans", Arial, sans-serif;
    position: relative;
  }
  .card {
    position: absolute;
    left: 182px;
    width: 746px;
    height: 426px;
  }
  .card--front { top: 119px; background: var(--card-white); }
  .card--back  { top: 637px; background: var(--green-dark); }

  .brand {
    position: absolute;
    left: 52px; top: 52px;
    display: flex; align-items: center; gap: 14px;
  }
  .brand__square {
    width: 44px; height: 44px;
    background: var(--green-light);
    flex: none;
  }
  .brand__text { display: flex; flex-direction: column; }
  .brand__name {
    font-weight: 600;
    font-size: 34px;
    color: var(--green-dark);
    line-height: 1.1;
  }
  .brand__slogan {
    font-size: 15px;
    letter-spacing: 3px;
    text-transform: uppercase;
    color: var(--green-light);
    line-height: 1.4;
  }

  .person {
    position: absolute;
    right: 50px; top: 84px;
    text-align: right;
  }
  .person__name {
    font-weight: 600; font-size: 27px;
    color: var(--green-dark); line-height: 36px;
  }
  .accent-bar {
    position: absolute;
    right: 0; top: 73px;
    width: 17px; height: 58px;
    background: var(--green-dark);
  }

  .contacts {
    position: absolute;
    left: 52px; top: 270px;
    list-style: none;
  }
  .contacts li {
    display: flex; align-items: center; gap: 8px;
    font-size: 19px; color: var(--text-grey);
    height: 28.5px;
  }
  .contacts svg { width: 19px; height: 19px; fill: var(--green-dark); flex: none; }

  .address {
    position: absolute;
    right: 50px; top: 297px;
    text-align: right;
    font-size: 19px; color: var(--text-grey);
    line-height: 29px;
    font-style: normal;
  }
  .address__web { margin-top: 3px; display: block; }

  .back__brand {
    position: absolute;
    left: 0; right: 0; top: 150px;
    display: flex; justify-content: center; align-items: center; gap: 18px;
  }
  .back__circle {
    width: 44px; height: 44px; border-radius: 50%;
    background: var(--text-light);
  }
  .back__name {
    font-weight: 600; font-size: 54px;
    color: var(--text-light); line-height: 1;
  }
  .back__web {
    position: absolute;
    left: 0; right: 0; top: 358px;
    text-align: center;
    font-size: 19px; letter-spacing: 4px;
    color: var(--text-light);
  }
</style>
</head>
<body>
  <section class="card card--front">
    <div class="brand">
      <span class="brand__square"></span>
      <div class="brand__text">
        <span class="brand__name">Brevel Coatings</span>
        <span class="brand__slogan">making change simple</span>
      </div>
    </div>

    <div class="person">
      <p class="person__name">Doran Vask</p>
    </div>
    <span class="accent-bar"></span>

    <ul class="contacts">
      <li>
        <svg viewBox="0 0 24 24" aria-hidden="true"><path d="M6.6 10.8a15.1 15.1 0 0 0 6.6 6.6l2.2-2.2c.3-.3.7-.4 1-.2 1.1.4 2.3.6 3.6.6.6 0 1 .4 1 1V20c0 .6-.4 1-1 1A17 17 0 0 1 3 4c0-.6.4-1 1-1h3.5c.6 0 1 .4 1 1 0 1.3.2 2.5.6 3.6.1.3 0 .7-.2 1l-2.3 2.2z"/></svg>
        555 416 9073
      </li>
      <li>
        <svg viewBox="0 0 24 24" aria-hidden="true"><path d="M7 1h10a2 2 0 0 1 2 2v18a2 2 0 0 1-2 2H7a2 2 0 0 1-2-2V3a2 2 0 0 1 2-2zm0 3v15h10V4H7zm5 16.2a.9.9 0 1 0 0 1.8.9.9 0 0 0 0-1.8z"/></svg>
        555 416 9074
      </li>
      <li>
        <svg viewBox="0 0 24 24" aria-hidden="true"><path d="M7 2h10v5H7zM4 8h16a2 2 0 0 1 2 2v7h-4v5H6v-5H2v-7a2 2 0 0 1 2-2zm4 8v4h8v-4H8z"/></svg>
        555 416 9075
      </li>
      <li>
        <svg viewBox="0 0 24 24" aria-hidden="true"><path d="M3 5h18v14H3V5zm2 2v.3l7 5 7-5V7H5zm0 2.8V17h14V9.8l-7 5-7-5z"/></svg>
        d.vask@brevel-coatings.com
      </li>
    </ul>

    <address class="address">
      1420 Larkspur Court<br>
      Fairview, Oregon 97024
      <span class="address__web">www.brevel-coatings.com</span>
    </address>
  </section>

  <section class="card card--back">
    <div class="back__brand">
      <span class="back__circle"></span>
      <span class="back__name">Brevel Coatings</span>
    </div>
    <p class="back__web">www.brevel-coatings.com</p>
  </section>
</body>
</html>
```